Business Card for a Candle Company. - Creative Hipster Styling :)

I am after a two sided Business Card. Contact information on the front, text that will be supplied (and details further on here) on the back. Ideally I am looking for someone I can continue to work with in the future for flyers, labels, marketing material etc.

I have a Logo which I am using as the labels for the candle and have attached all the versions of the file I was given. I am after a similar feel to my logo and love the font and the feather used. it is important that my card looks like it is meant to go with the logo.

I would love you to use your imagination and see what can be thought up :)

All my candles are either clear or black glass and packaging is black and labels are white, on a square label with black writing (see attachments)

I love the feather on the logo if it can be incorporated great, if the business card looks better without it than that is fine too..

Target Market(s)

I am a new candle company and the feel I'm going for is a little luxury a little hipster. Imagine the candle going into a converted warehouse studio in the city.

Industry/Entity Type

Home And Garden

Contact Information for Business Card

I have a Logo which I am using as the labels for the candle and have attached all the versions of the file I was given. I am after a similar feel to my logo and love the font used but its caps and I don't really want everything in CAPS. It is important thought that everything goes together.

I love the feather on the logo if it can be incorporated great, if the business card looks better without it than that is fine too.

Morrel Wick Co
Driftwood Bay, Eastshore
A small candle studio, in a shed, by the sea.
craftlane.example/au/shop/MorrelWickCo
friendspace.example.au/morrelwickco
morrelwickco@mailbox.example.au
Jess Holloran
0481 572 316.

On the back of the card I need it to look good and go with the design on the front but want a bit of text;

To give you an idea of what I want on the back I've put what I've got following but I'm still working on grammar and wording so it may change slightly before the final edit.

We would love to see how you display your candle or reuse the glass vessel and would love to see a photo!
Check out ideas and share yours on your social media #morrelwickco

Just a few ideas to reuse your vessel;

A Vase to Display fresh flowers
Lolly Jar for your favourite candy
Decorate with baubles at Christmas
Bathroom Vanity Storage
Decorate with eggs at Easter
Plant a teranium inside.

Font styles to use
Decorative
Script
Other font styles liked:
• OctinVintageFree

Colors
000000
ffffff
757575

Requirements
Must have
• The only must is that it needs to look like it goes with my logo which I am using as the labels on the actual candle. the labels are white with black details and are square.
• Not too structured if possible as it is a creative company rather that a professional services company.
• I want people to pick up the card and think it looks great. I believe a business card is a very useful marketing tool and should be used as such. One card will be included in with each candle so that customers can re order.
Nice to have
• I love the feather on the logo if it can be incorporated great, if the business card looks better without it than that is fine too.
• Card just needs to fit with the logo.
Should not have
• It should not be a boring card. :)

```html
<!DOCTYPE html>
<html lang="en">
<head>
<meta charset="utf-8">
<title>Morrel Wick Co — Business Card</title>
<link rel="stylesheet" href="https://fonts.googleapis.com/css2?family=Roboto+Slab:wght@400;700&display=swap">
<style>
  :root {
    --ink: #000000;
    --paper: #ffffff;
    --grey: #757575;
    --soft: #d8d8d8;
    --backdrop: #e9e6e1;
  }
  * { margin: 0; padding: 0; box-sizing: border-box; }
  html, body { width: 1200px; height: 913px; overflow: hidden; }
  body {
    background: var(--backdrop);
    font-family: "Roboto Slab", Georgia, serif;
    position: relative;
  }
  .card {
    position: absolute;
    width: 520px;
    height: 297px;
    border-radius: 16px;
    overflow: hidden;
    box-shadow: 0 10px 28px rgba(0,0,0,0.22);
  }
  .card--front { left: 60px; top: 308px; background: var(--ink); color: var(--paper); }
  .card--back { left: 620px; top: 308px; background: var(--paper); color: var(--ink); }

  .card__art { position: absolute; inset: 0; width: 100%; height: 100%; }

  .brand-name {
    position: absolute;
    font-weight: 400;
    letter-spacing: 0.12em;
    text-transform: uppercase;
    white-space: nowrap;
  }
  .card--front .brand-name {
    left: 0; width: 260px; top: 130px;
    text-align: center; font-size: 20px; color: var(--paper);
  }
  .card--back .brand-name {
    left: 0; right: 0; top: 58px;
    text-align: center; font-size: 24px; color: var(--ink);
  }

  .contact {
    position: absolute;
    right: 22px; top: 44px;
    width: 228px;
    text-align: right;
  }
  .contact__name { font-weight: 700; font-size: 17px; line-height: 1.1; }
  .contact__role { font-size: 10px; color: var(--soft); margin-top: 3px; }
  .contact__list { list-style: none; margin-top: 10px; }
  .contact__item {
    display: flex; justify-content: flex-end; align-items: center; gap: 6px;
    font-size: 9.5px; line-height: 17px; white-space: nowrap;
  }
  .icon { width: 10px; height: 10px; flex: none; }
  .contact__address { margin-top: 8px; font-size: 9.5px; line-height: 15px; padding-right: 16px; }

  .reuse-ideas {
    position: absolute;
    left: 0; right: 0; top: 130px;
    list-style: none;
    text-align: center;
    font-weight: 700;
    font-size: 13px;
    line-height: 19px;
  }
</style>
</head>
<body>

  <section class="card card--front" aria-label="Business card front">
    <svg class="card__art" viewBox="0 0 520 297" aria-hidden="true">
      <defs>
        <linearGradient id="front-gloss" x1="0" y1="0" x2="1" y2="0">
          <stop offset="0" stop-color="#000"/>
          <stop offset="0.35" stop-color="#3a3a3a"/>
          <stop offset="0.5" stop-color="#0c0c0c"/>
          <stop offset="1" stop-color="#000"/>
        </linearGradient>
        <linearGradient id="panel-grey" x1="0" y1="0" x2="1" y2="1">
          <stop offset="0" stop-color="#5a5a5a"/>
          <stop offset="0.5" stop-color="#2e2e2e"/>
          <stop offset="1" stop-color="#1a1a1a"/>
        </linearGradient>
      </defs>
      <rect width="520" height="297" fill="url(#front-gloss)"/>
      <path d="M300 0 Q 230 150 292 297 L520 297 L520 0 Z" fill="url(#panel-grey)"/>
      <path d="M300 0 Q 230 150 292 297" fill="none" stroke="#fff" stroke-width="7"/>
    </svg>

    <p class="brand-name">Morrel Wick Co</p>

    <div class="contact">
      <p class="contact__name">Jess Holloran</p>
      <p class="contact__role">Owner</p>
      <ul class="contact__list">
        <li class="contact__item">0481 572 316
          <svg class="icon" viewBox="0 0 10 10" aria-hidden="true"><path d="M2 1 L4 1 L4.6 3 L3.4 3.8 Q4.2 5.8 6.2 6.6 L7 5.4 L9 6 L9 8 Q5 9.5 1.5 4.5 Q1 2.5 2 1 Z" fill="#fff"/></svg>
        </li>
        <li class="contact__item">morrelwickco@mailbox.example.au
          <svg class="icon" viewBox="0 0 10 10" aria-hidden="true"><rect x="0.8" y="2" width="8.4" height="6" fill="none" stroke="#fff" stroke-width="1"/><path d="M0.8 2 L5 5.5 L9.2 2" fill="none" stroke="#fff" stroke-width="1"/></svg>
        </li>
        <li class="contact__item">friendspace.example.au/morrelwickco
          <svg class="icon" viewBox="0 0 10 10" aria-hidden="true"><circle cx="5" cy="5" r="4" fill="#fff"/></svg>
        </li>
        <li class="contact__item">craftlane.example/au/shop/MorrelWickCo
          <svg class="icon" viewBox="0 0 10 10" aria-hidden="true"><circle cx="5" cy="5" r="4" fill="none" stroke="#fff"/><ellipse cx="5" cy="5" rx="1.8" ry="4" fill="none" stroke="#fff" stroke-width="0.8"/><path d="M1 5 H9" stroke="#fff" stroke-width="0.8"/></svg>
        </li>
      </ul>
      <p class="contact__address">Driftwood Bay, Eastshore<br>A small candle studio, in a shed, by the sea.</p>
    </div>
  </section>

  <section class="card card--back" aria-label="Business card back">
    <p class="brand-name">Morrel Wick Co</p>
    <ul class="reuse-ideas">
      <li>A Vase to Display fresh flowers</li>
      <li>Lolly Jar for your favourite candy</li>
      <li>Decorate with baubles at Christmas</li>
      <li>Bathroom Vanity Storage</li>
      <li>Decorate with eggs at Easter</li>
      <li>Plant a teranium inside.</li>
    </ul>
  </section>

</body>
</html>
```